Non Profit raising scholarship funds needs flyer for Golf Tournament

We need a flyer for our upcoming golf tournament. Proceeds to will help to benefit our Pathway builders learning grant fund.

Title: 2019 O-RamVT Golf Tournament
Location: Brindle Oaks Links
Date: May 15, 2019
Registration: $175 individual, $700 foursome
Sponsorships starting at $250
Benefiting O-RamVT and the Pathway Builders Learning Grant Fund

Target Market(s)

Design and Construction industry professionals

Industry/Entity Type

Construction

Font styles to use
Serif
Sans Serif

Colors

Designer to choose colors to be used in the design.

Requirements
Must have
• Title, date, location, registration info, sponsor info, benefit info, logo
Nice to have
• I like the retro look of some golf flyers, but it's not necessary
Should not have
• .

```html
<!DOCTYPE html>
<html lang="en">
<head>
<meta charset="utf-8">
<title>2019 O-RamVT Golf Tournament</title>
<link rel="stylesheet" href="https://fonts.googleapis.com/css2?family=Montserrat:wght@400;500;600;700;800&display=swap">
<style>
  :root {
    --teal: #3a9b93;
    --teal-light: #48ab9e;
    --sky: #2f96c4;
    --leaf: #53ad46;
    --leaf-light: #63b74c;
    --lime: #7ed957;
    --accent-blue: #2fa9ea;
    --accent-yellow: #d5e222;
    --grass-dark: #2c6420;
    --grass-light: #5f9e3c;
    --white: #f4f4f4;
  }
  html, body {
    margin: 0;
    padding: 0;
    width: 848px;
    height: 1200px;
    overflow: hidden;
    background: #ffffff;
  }
  .flyer {
    position: relative;
    width: 848px;
    height: 1200px;
    overflow: hidden;
  }
  .stage {
    position: absolute;
    left: 0;
    top: 0;
    width: 794px;
    height: 1123px;
    transform: scale(1.068, 1.0686);
    transform-origin: 0 0;
    font-family: "Montserrat", sans-serif;
    color: var(--white);
  }
  .backdrop {
    position: absolute;
    inset: 0;
    width: 794px;
    height: 1123px;
  }
  .brand {
    position: absolute;
    left: 455px;
    top: 16px;
    display: flex;
    align-items: center;
    gap: 14px;
  }
  .brand-mark {
    width: 76px;
    height: 76px;
    border-radius: 50%;
    background: var(--white);
  }
  .brand-name {
    font-size: 50px;
    font-weight: 500;
    letter-spacing: 1px;
    line-height: 1;
    color: var(--white);
  }
  .year {
    position: absolute;
    left: 86px;
    top: 170px;
    margin: 0;
    font-size: 226px;
    font-weight: 800;
    line-height: 1;
    letter-spacing: -2px;
  }
  .title {
    position: absolute;
    left: 262px;
    top: 384px;
    margin: 0;
    font-size: 61px;
    font-weight: 700;
    line-height: 58px;
    text-transform: uppercase;
  }
  .registration {
    position: absolute;
    left: 87px;
    top: 672px;
  }
  .label {
    margin: 0;
    font-size: 30px;
    font-weight: 700;
    color: var(--accent-yellow);
    letter-spacing: 0.5px;
    line-height: 36px;
  }
  .detail {
    margin: 0;
    font-size: 27px;
    font-weight: 500;
    letter-spacing: 3px;
    line-height: 38px;
    text-transform: uppercase;
  }
  .registration .detail { margin-top: 4px; }
  .sponsorship {
    position: absolute;
    left: 87px;
    top: 846px;
  }
  .sponsorship .detail { line-height: 42px; }
  .event-info {
    position: absolute;
    right: 46px;
    top: 668px;
    margin: 0;
    text-align: right;
    font-size: 36px;
    font-weight: 700;
    line-height: 49px;
    text-transform: uppercase;
  }
  .benefit {
    position: absolute;
    left: 0;
    width: 794px;
    top: 990px;
    margin: 0;
    text-align: center;
    font-size: 23.5px;
    font-weight: 600;
    letter-spacing: 0.6px;
    line-height: 38px;
    text-transform: uppercase;
  }
  .more-info {
    position: absolute;
    left: 0;
    width: 794px;
    top: 1070px;
    margin: 0;
    text-align: center;
    font-size: 15px;
    font-weight: 500;
    color: var(--accent-yellow);
    letter-spacing: 0.3px;
    text-transform: uppercase;
  }
</style>
</head>
<body>
<main class="flyer">
  <div class="stage">
    <svg class="backdrop" viewBox="0 0 794 1123" xmlns="http://www.w3.org/2000/svg">
      <defs>
        <linearGradient id="grass" x1="0" y1="0" x2="0" y2="1">
          <stop offset="0" stop-color="var(--grass-light)"/>
          <stop offset="1" stop-color="var(--grass-dark)"/>
        </linearGradient>
      </defs>
      <rect class="base" width="794" height="1123" fill="var(--teal)"/>
      <polygon class="panel-teal-light" points="80,0 420,0 520,300 330,560 80,600" fill="var(--teal-light)" opacity="0.6"/>
      <polygon class="panel-sky" points="0,0 85,0 85,612 0,606" fill="var(--sky)"/>
      <polygon class="panel-sky-wedge" points="0,120 260,520 0,600" fill="var(--sky)" opacity="0.55"/>
      <polygon class="panel-leaf" points="400,0 794,0 794,860 560,790 330,430" fill="var(--leaf)"/>
      <polygon class="panel-leaf-light" points="430,0 700,0 560,260" fill="var(--leaf-light)"/>
      <polygon class="panel-leaf-light" points="794,300 794,700 620,560" fill="var(--leaf-light)" opacity="0.7"/>
      <g role="img" aria-label="Photograph of a golf ball resting at the edge of the hole on a putting green">
        <polygon class="green-photo" points="0,606 330,560 560,790 794,860 794,1123 0,1123" fill="url(#grass)"/>
      </g>
      <rect class="bar-top" x="314" y="98" width="480" height="20" fill="var(--accent-blue)"/>
      <rect class="bar-title" x="0" y="418" width="244" height="62" fill="var(--lime)"/>
      <polygon class="tick-year" points="67,213 98,213 82,238" fill="var(--accent-yellow)"/>
      <polygon class="tick-date" points="512,628 544,628 528,655" fill="var(--accent-yellow)"/>
      <rect class="bar-venue" x="550" y="849" width="195" height="13" fill="var(--accent-blue)"/>
      <polygon class="tick-sponsor" points="378,963 442,963 410,915" fill="var(--accent-blue)"/>
    </svg>

    <div class="brand">
      <span class="brand-mark"></span>
      <span class="brand-name">O-RamVT</span>
    </div>

    <h1 class="year">2019</h1>
    <h2 class="title">O-RamVT Golf<br>Tournament</h2>

    <section class="registration">
      <p class="label">REGISTRATION</p>
      <p class="detail">$175 individual,<br>$700 foursome</p>
    </section>

    <section class="sponsorship">
      <p class="detail">Sponsorships<br>starting at $250</p>
    </section>

    <p class="event-info">May 15, 2019<br>Brindle Oaks<br>Links</p>

    <p class="benefit">Benefiting O-RamVT and the<br>Pathway Builders Learning Grant Fund</p>
    <p class="more-info">Visit o-ramvt.org for more information</p>
  </div>
</main>
</body>
</html>
```